Velmor Stationery Design

We need Business Card, Letterhead, #10 Envelope , 3" x 4" Mailing Label, and email signature block. Also need "Aircraft Services" added small under the logo on everything except the email signature block. "Aircraft Services" should be in a simple font to to conflict with or distract from the logo. Our address info is:
4817 Halvend Loop NW
Brantwick, GA 30592
P 555.208.3146
C 555.208.3146 (for biz cards only)
glen@velmorjet.example (for biz cards only)
Website velmorjet.example
Feel free to play around with colors but I expect that black or gray will work best for the address/phone info etc.

Target Market(s)

Aircraft owners

Industry/Entity Type

Aviation

Colors

Designer to choose only greyscale colors for use in the design.

Requirements
Must have
• Clean and sophisticated design -

```html
<!DOCTYPE html>
<html lang="en">
<head>
<meta charset="utf-8">
<title>Velmor Business Card</title>
<link rel="stylesheet" href="https://fonts.googleapis.com/css2?family=Montserrat:wght@400;500;600;700&display=swap">
<style>
  :root {
    --stage: #bdbcb8;
    --card-white: #ffffff;
    --card-black: #1c1c1d;
    --accent-grey: #8c8c8c;
    --brand-dark: #2e2e2f;
    --brand-light: #d6d6d6;
    --text-light: #f2f2f2;
    --text-dark: #1c1c1d;
    --text-muted: #6a6a6a;
  }
  * { margin: 0; padding: 0; box-sizing: border-box; }
  html, body { width: 1200px; height: 857px; overflow: hidden; }
  body {
    background: var(--stage);
    font-family: "Montserrat", sans-serif;
    position: relative;
  }
  .card {
    position: absolute;
    top: 268px;
    width: 560px;
    height: 320px;
    border-bottom: 4px solid var(--accent-grey);
    box-shadow: 0 14px 30px rgba(0,0,0,0.25);
    overflow: hidden;
  }
  .card-front { left: 27px; background: var(--card-white); }
  .card-back { left: 613px; background: var(--card-black); }

  .front-shape { position: absolute; inset: 0; }

  .brand-lockup {
    position: absolute;
    text-align: center;
  }
  .wordmark {
    display: block;
    font-weight: 700;
    text-transform: uppercase;
    letter-spacing: 2px;
    line-height: 1;
  }
  .tagline {
    display: block;
    font-weight: 500;
    text-transform: uppercase;
    letter-spacing: 3px;
    line-height: 1;
  }
  .card-front .brand-lockup { left: 40px; top: 118px; }
  .card-front .wordmark { font-size: 40px; color: var(--brand-dark); }
  .card-front .tagline { font-size: 10px; color: var(--text-muted); margin-top: 10px; }

  .identity {
    position: absolute;
    left: 300px;
    top: 22px;
    padding-left: 12px;
    border-left: 2px solid var(--accent-grey);
  }
  .identity-name {
    color: var(--brand-dark);
    font-weight: 600;
    font-size: 17px;
    letter-spacing: 0.5px;
  }
  .identity-title {
    color: var(--text-muted);
    font-size: 11px;
    margin-top: 2px;
  }

  .contact {
    position: absolute;
    left: 318px;
    top: 128px;
    color: var(--text-light);
    font-size: 12px;
    line-height: 1.55;
    list-style: none;
  }
  .contact-address { margin-bottom: 8px; }
  .contact-row { display: flex; align-items: center; gap: 8px; }
  .contact-row svg { width: 11px; height: 11px; flex: none; }

  .brand-pattern {
    position: absolute;
    inset: 0;
    background: linear-gradient(135deg, #1a1a1b 0%, #262627 50%, #1c1c1d 100%);
  }
  .card-back .brand-lockup { left: 0; right: 0; top: 200px; }
  .card-back .wordmark { font-size: 30px; color: var(--brand-light); }
  .card-back .tagline { font-size: 9px; color: var(--accent-grey); margin-top: 8px; }
</style>
</head>
<body>
  <section class="card card-front" aria-label="Business card front">
    <svg class="front-shape" viewBox="0 0 560 320" width="560" height="320" aria-hidden="true">
      <path d="M560,60 L560,320 L150,320 C112,240 250,120 560,60 Z" fill="var(--card-black)"/>
      <path d="M560,60 C250,120 112,240 150,320" fill="none" stroke="var(--accent-grey)" stroke-width="7"/>
      <path d="M150,320 C170,300 230,290 300,250" fill="none" stroke="var(--accent-grey)" stroke-width="4"/>
    </svg>

    <div class="brand-lockup">
      <span class="wordmark">Velmor</span>
      <span class="tagline">Aircraft Services</span>
    </div>

    <div class="identity">
      <div class="identity-name">MARTIN CALDWELL</div>
      <div class="identity-title">Development Manager Officer</div>
    </div>

    <ul class="contact">
      <li class="contact-address">4817 Halvend Loop NW<br>Brantwick, GA 30592</li>
      <li class="contact-row">
        <svg viewBox="0 0 12 12"><path d="M2 1h3l1 3-1.5 1a7 7 0 0 0 2.5 2.5L8 6l3 1v3a1 1 0 0 1-1 1A9 9 0 0 1 1 2a1 1 0 0 1 1-1z" fill="var(--accent-grey)"/></svg>
        555.208.3146
      </li>
      <li class="contact-row">
        <svg viewBox="0 0 12 12"><rect x="3" y="0.5" width="6" height="11" rx="1" fill="none" stroke="var(--accent-grey)" stroke-width="1.2"/><circle cx="6" cy="9.5" r="0.7" fill="var(--accent-grey)"/></svg>
        555.208.3146
      </li>
      <li class="contact-row">
        <svg viewBox="0 0 12 12"><rect x="0.5" y="2" width="11" height="8" fill="var(--accent-grey)"/><path d="M0.5 2l5.5 4.5L11.5 2" fill="none" stroke="var(--card-black)" stroke-width="1"/></svg>
        glen@velmorjet.example
      </li>
      <li class="contact-row">
        <svg viewBox="0 0 12 12"><circle cx="6" cy="6" r="5" fill="none" stroke="var(--accent-grey)" stroke-width="1.2"/><path d="M1 6h10M6 1c-3 3-3 7 0 10M6 1c3 3 3 7 0 10" fill="none" stroke="var(--accent-grey)" stroke-width="1"/></svg>
        velmorjet.example
      </li>
    </ul>
  </section>

  <section class="card card-back" aria-label="Business card back">
    <div class="brand-pattern" role="img" aria-label="Tone-on-tone embossed repeating brand pattern"></div>
    <div class="brand-lockup">
      <span class="wordmark">Velmor</span>
      <span class="tagline">Aircraft Services</span>
    </div>
  </section>
</body>
</html>
```